Job Coaching - Vanta; engaging people to improve their work experience

I need a flyer for Job Coaching. It serves to engage customers (not businesses) with problems in their daily job, typical questions that are handled are:
Do I fit for the job?
Am I using my talents at best in this job?
I have a conflict with my manager/colleagues, what should I do?
My work-life balance is a mess, how can I improve this?
What job fits best with my talents?
I'm getting stressed out from my job, what can I do?
....
This Flyer will be available at GP's, therpeutic practices, pharamcists,...
this flyer should put people in action to contact me
Flyer can be created in English, in the final one the text should be in Dutch; I will make the translation of the selected flyer and provide it at the end

Target Market(s)

consumers / customers / people having a job, but somewhat stuck in it

Industry/Entity Type

Professional Coaching

Requirements
Must have
• the questions mentioned in the project description; mobile number: 0471/389145; email: tom.vermeer@vantacoaching.example; website: www.vantacoaching.example ; it should make also reference to 'Career guidance cheques of the KWOL'

```html
<!DOCTYPE html>
<html lang="en">
<head>
<meta charset="utf-8">
<title>Vanta – Career Guidance Flyer</title>
<link href="https://fonts.googleapis.com/css2?family=Montserrat:wght@400;500;600;700&display=swap" rel="stylesheet">
<style>
  :root {
    --backdrop: #2e2e2e;
    --paper: #f4f5f6;
    --teal: #38aea3;
    --teal-dark: #25857c;
    --ink: #5a5a5c;
    --ink-strong: #4a4a4c;
    --photo-warm: #a8764f;
    --photo-shirt: #8e2332;
  }
  * { box-sizing: border-box; margin: 0; padding: 0; }
  html, body {
    width: 1200px; height: 1200px; overflow: hidden;
    background: var(--backdrop);
    font-family: "Montserrat", sans-serif;
    color: var(--ink);
  }
  .flyer {
    position: absolute; left: 216px; top: 64px;
    width: 764px; height: 1071px; overflow: hidden;
    background: linear-gradient(160deg, #fafafa 0%, var(--paper) 55%, #eceeef 100%);
    box-shadow: 0 6px 18px rgba(0,0,0,.45);
  }
  .portrait {
    position: absolute; left: 0; top: 0; width: 324px; height: 100%;
    background:
      linear-gradient(180deg, rgba(0,0,0,0) 0%, rgba(0,0,0,0) 88%, #1f1c22 100%),
      linear-gradient(180deg, #c9a98a 0%, var(--photo-warm) 28%, #9a3a3f 42%, var(--photo-shirt) 60%, #7a1e2b 90%);
  }
  .content { position: absolute; left: 324px; top: 0; width: 440px; height: 100%; }

  .brand {
    position: absolute; left: 0; right: 0; top: 24px;
    display: flex; align-items: center; justify-content: center; gap: 12px;
  }
  .brand-dot { width: 62px; height: 62px; border-radius: 50%; background: var(--teal); }
  .brand-text { display: flex; flex-direction: column; }
  .brand-name { font-weight: 600; font-size: 56px; line-height: 1; color: var(--teal); letter-spacing: 1px; }
  .brand-tag { font-weight: 600; font-size: 12px; color: #666; margin-top: 2px; }

  .title { position: absolute; left: 21px; right: 23px; top: 141px; text-align: center; }
  .title h1 { font-weight: 700; font-size: 34px; line-height: 40px; color: var(--teal); white-space: nowrap; }
  .title p { font-weight: 500; font-size: 19.5px; line-height: 24px; color: var(--ink-strong); }

  .copy {
    position: absolute; left: 21px; width: 397px;
    font-size: 12.9px; line-height: 18.6px; letter-spacing: -0.1px; text-align: justify;
  }
  .copy strong { font-weight: 700; color: var(--ink-strong); }
  .copy-intro { top: 231px; }
  .copy-purpose { top: 319px; }
  .copy-career { top: 402px; }
  .copy-focus { top: 557px; }
  .lead {
    position: absolute; left: 21px; width: 397px; top: 506px;
    font-weight: 700; font-size: 17px; line-height: 21px; color: var(--teal);
  }

  .band {
    position: absolute; left: -13px; right: 0;
    background: var(--teal); color: #fff; font-weight: 700;
  }
  .band::after {
    content: ""; position: absolute; left: 0; bottom: -9px;
    border-top: 9px solid var(--teal-dark); border-left: 13px solid transparent;
  }
  .band-questions { top: 607px; height: 40px; font-size: 15px; line-height: 18.5px; padding: 2px 22px 0 34px; text-align: justify; }
  .band-contact { top: 923px; height: 23px; font-size: 15px; line-height: 23px; padding-left: 35px; }
  .band-reference { top: 1002px; height: 23px; font-size: 15px; line-height: 23px; padding-left: 35px; }

  .questions {
    position: absolute; left: 21px; width: 397px; top: 656px;
    list-style: none; font-size: 13px; line-height: 18.6px; letter-spacing: -0.1px;
  }
  .questions li { position: relative; padding-left: 16px; margin-bottom: 4.6px; }
  .questions li::before {
    content: ""; position: absolute; left: 2px; top: 7px;
    width: 6px; height: 6px; border-radius: 50%; background: var(--teal);
  }

  .closing {
    position: absolute; left: 21px; top: 862px;
    font-weight: 700; font-size: 21px; line-height: 26px; color: var(--teal); white-space: nowrap;
  }
  .closing span { color: var(--ink-strong); }
  .closing-rule { position: absolute; left: 98px; top: 896px; width: 229px; height: 3px; background: #666; }

  .contact-item {
    position: absolute; display: flex; align-items: center; gap: 6px;
    font-size: 13.5px; line-height: 20px; white-space: nowrap;
  }
  .contact-item svg { width: 13px; height: 13px; flex: none; }
  .contact-phone { left: 21px; top: 950px; }
  .contact-email { left: 150px; top: 950px; }
  .contact-web { left: 21px; top: 972px; }

  .reference { position: absolute; left: 23px; top: 1029px; font-size: 13.5px; line-height: 18px; }
</style>
</head>
<body>
  <main class="flyer">
    <div class="portrait" role="img" aria-label="Photo of the coach smiling, wearing glasses and a dark red shirt, standing indoors"></div>

    <section class="content">
      <div class="brand">
        <div class="brand-dot"></div>
        <div class="brand-text">
          <span class="brand-name">VANTA</span>
          <span class="brand-tag">professional coaching</span>
        </div>
      </div>

      <header class="title">
        <h1>TAB - Career Guidance</h1>
        <p>(with Career Vouchers)</p>
      </header>

      <p class="copy copy-intro">We easily spend 8 hours a day on our professional pursuits, our job. If we assume that we sleep about 8 hours a day, that's 50% of our active time. We actually spend more time with our colleagues than with our partner and/or children.</p>
      <p class="copy copy-purpose">So we'd better make sure that we spend those 8 hours meaningfully and, at best, get energy from it too. That we can accomplish a piece of our personal accomplishments there.</p>
      <p class="copy copy-career">Unfortunately, not every career goes smoothly, and it is even very normal that there are ups and downs this, nowadays more than 40-year career. But we can strive to keep these downs as short as possible and the ups as long as possible.</p>
      <h2 class="lead">And that's where Career Counseling comes into play.</h2>
      <p class="copy copy-focus">During this career counseling, we take a close look at your <strong>personal situation</strong>.</p>

      <div class="band band-questions">Do you recognize yourself in any of the following questions?</div>

      <ul class="questions">
        <li>How can I get more energy from my job?</li>
        <li>How can I get a better work-life balance?</li>
        <li>What are my talents?</li>
        <li>How can I work better with my manager and/or colleagues?</li>
        <li>Do you know what you want, but do not dare to take the step?</li>
        <li>Or maybe you think you have more up your sleeve than you do today?</li>
      </ul>

      <p class="closing">Then we will work on this <span>together.</span></p>
      <div class="closing-rule"></div>

      <div class="band band-contact">Contact:</div>
      <div class="contact-item contact-phone">
        <svg viewBox="0 0 14 14" aria-hidden="true"><circle cx="7" cy="7" r="7" fill="var(--teal)"/><rect x="4.6" y="3" width="4.8" height="8" rx="1" fill="none" stroke="#fff" stroke-width="1.2"/></svg>
        <span>0471/389145</span>
      </div>
      <div class="contact-item contact-email">
        <svg viewBox="0 0 14 14" aria-hidden="true"><circle cx="7" cy="7" r="7" fill="var(--teal)"/><rect x="3.5" y="4.5" width="7" height="5" fill="none" stroke="#fff" stroke-width="1.1"/><path d="M3.5 4.5 7 7.4 10.5 4.5" fill="none" stroke="#fff" stroke-width="1.1"/></svg>
        <span>tom.vermeer@vantacoaching.example</span>
      </div>
      <div class="contact-item contact-web">
        <svg viewBox="0 0 14 14" aria-hidden="true"><circle cx="7" cy="7" r="7" fill="var(--teal)"/><circle cx="7" cy="7" r="3.8" fill="none" stroke="#fff" stroke-width="1"/><path d="M3.2 7h7.6M7 3.2c-2 2.4-2 5.2 0 7.6M7 3.2c2 2.4 2 5.2 0 7.6" fill="none" stroke="#fff" stroke-width=".9"/></svg>
        <span>www.vantacoaching.example</span>
      </div>

      <div class="band band-reference">Reference:</div>
      <p class="reference">Career guidance cheques of the KWOL</p>
    </section>
  </main>
</body>
</html>
```